Business Card Design for Photographer

Updating business card design. Must use included logo. We're a luxury wedding photography business. Elegancy, luxury, consistency are messages we wish to convey.

Visit our website at www.colvanderose.com to familiarize yourself more with our brand design currently (fonts, colors etc.). This is what we want to maintain.

Target Market(s)

Luxury Brides and Grooms

Industry/Entity Type

Wedding

Contact Information for Business Card

Current logo (attached to brief)
Name: Colin Vanderose
Phone: 5871302948
website/blog
Email

Requirements
Must have
• Current logo (attached to brief)
• Name: Colin Vanderose
• Phone: 5871302948
• website/blog
• Email
• Social username
Should not have
• bright colors, fonts that don't suit our brand (visit www.colvanderose.com)

```html
<!DOCTYPE html>
<html lang="en">
<head>
<meta charset="utf-8">
<title>Colin Vanderose Photographers – Business Card</title>
<link href="https://fonts.googleapis.com/css2?family=Josefin+Sans:wght@300;400&family=Lato:wght@300;400&display=swap" rel="stylesheet">
<style>
  :root {
    --page: #ffffff;
    --card: #f6f7f9;
    --panel: #eff0f2;
    --band: #dcdde0;
    --ink: #6f6f71;
    --mark: #767676;
    --shadow: rgba(0,0,0,0.22);
  }
  * { margin: 0; padding: 0; box-sizing: border-box; }
  html, body { width: 1200px; height: 900px; overflow: hidden; background: var(--page); }
  .canvas { position: relative; width: 1200px; height: 900px; }

  .card { position: absolute; background: var(--card); box-shadow: 2px 4px 6px var(--shadow); }
  .card-front { left: 116px; top: 83px; width: 742px; height: 452px; }
  .card-back { left: 399px; top: 414px; width: 683px; height: 416px; }

  .brand-panel {
    position: absolute; left: 217px; top: 48px; width: 324px; height: 135px;
    background: var(--panel); text-align: center;
  }
  .brand-square { position: absolute; left: 140px; top: 7px; width: 48px; height: 48px; background: var(--mark); }
  .brand-name {
    position: absolute; left: 0; right: 0; top: 74px;
    font-family: "Josefin Sans", sans-serif; font-weight: 300;
    font-size: 23px; line-height: 28px; letter-spacing: 4px; color: var(--ink); text-transform: uppercase;
    white-space: nowrap;
  }
  .brand-tagline {
    position: absolute; left: 0; right: 0; top: 109px;
    font-family: "Josefin Sans", sans-serif; font-weight: 400;
    font-size: 12px; line-height: 16px; letter-spacing: 4.5px; color: var(--ink); text-transform: uppercase;
  }

  .band { position: absolute; top: 209px; height: 207px; background: var(--band); }
  .band-left { left: 0; width: 204px; }
  .band-right { left: 539px; width: 203px; }

  .photo { position: absolute; }
  .photo-car { left: 210px; top: 210px; width: 158px; height: 102px; background: linear-gradient(160deg, #5f7347, #9da08d 55%, #cfd0cb); }
  .photo-tent { left: 371px; top: 210px; width: 77px; height: 102px; background: linear-gradient(180deg, #e9eae6, #9d9a7d 60%, #6a6147); }
  .photo-garden { left: 451px; top: 210px; width: 78px; height: 102px; background: linear-gradient(180deg, #d8e2d2, #566b3c 45%, #9d9c96); }
  .photo-aisle { left: 210px; top: 315px; width: 77px; height: 101px; background: linear-gradient(180deg, #6f8456, #c9cbbf 60%, #b8c1a7); }
  .photo-bouquet { left: 290px; top: 315px; width: 78px; height: 101px; background: radial-gradient(circle at 50% 40%, #e9a896, #a9a79a 45%, #5c4b3f); }
  .photo-beach { left: 371px; top: 315px; width: 158px; height: 101px; background: linear-gradient(180deg, #e4eef2, #bfd7dc 40%, #ece6dc 70%, #f2eee8); }

  .back-mark { position: absolute; left: 561px; top: 23px; width: 95px; height: 76px; background: var(--panel); }
  .back-mark-square { position: absolute; left: 17px; top: 10px; width: 42px; height: 42px; background: var(--mark); }
  .back-mark-name {
    position: absolute; left: 0; right: 0; top: 58px; text-align: center;
    font-family: "Josefin Sans", sans-serif; font-weight: 300;
    font-size: 8px; line-height: 10px; letter-spacing: 1px; color: var(--ink); text-transform: uppercase;
    white-space: nowrap;
  }

  .holder-name {
    position: absolute; left: 63px; top: 174px; width: 333px; height: 34px;
    background: var(--panel); padding-left: 9px;
    font-family: "Josefin Sans", sans-serif; font-weight: 300;
    font-size: 26px; line-height: 36px; letter-spacing: 4px; color: var(--ink); text-transform: uppercase;
    white-space: nowrap;
  }

  .contact-list { position: absolute; left: 72px; top: 220px; list-style: none; }
  .contact-item {
    display: flex; align-items: center; height: 32.5px;
    font-family: "Lato", sans-serif; font-weight: 400; font-size: 18px; color: var(--ink);
    white-space: nowrap;
  }
  .contact-icon { width: 28px; height: 28px; margin-right: 16px; flex: none; }
</style>
</head>
<body>
<div class="canvas">

  <section class="card card-front" aria-label="Card front">
    <div class="brand-panel">
      <span class="brand-square" aria-hidden="true"></span>
      <div class="brand-name">Colin Vanderose</div>
      <div class="brand-tagline">Photographers</div>
    </div>
    <div class="band band-left"></div>
    <div class="band band-right"></div>
    <div class="photo photo-car" role="img" aria-label="Wedding couple kissing beside a vintage white car in a garden"></div>
    <div class="photo photo-tent" role="img" aria-label="Long reception table under a white draped tent"></div>
    <div class="photo photo-garden" role="img" aria-label="Couple walking hand in hand between tall cypress hedges"></div>
    <div class="photo photo-aisle" role="img" aria-label="Outdoor ceremony aisle leading to a white gazebo"></div>
    <div class="photo photo-bouquet" role="img" aria-label="Bridal bouquet of peach roses and greenery"></div>
    <div class="photo photo-beach" role="img" aria-label="Bride and groom embracing on a sandy beach"></div>
  </section>

  <section class="card card-back" aria-label="Card back">
    <div class="back-mark">
      <span class="back-mark-square" aria-hidden="true"></span>
      <div class="back-mark-name">Colin Vanderose</div>
    </div>
    <div class="holder-name">Colin Vanderose</div>
    <ul class="contact-list">
      <li class="contact-item">
        <svg class="contact-icon" viewBox="0 0 28 28" aria-hidden="true">
          <rect x="5" y="3" width="15" height="23" rx="3" transform="rotate(-12 12 14)" fill="none" stroke="#6f6f71" stroke-width="2"/>
          <circle cx="15" cy="21" r="1.4" fill="#6f6f71"/>
        </svg>
        5871302948
      </li>
      <li class="contact-item">
        <svg class="contact-icon" viewBox="0 0 28 28" aria-hidden="true">
          <text x="14" y="21" text-anchor="middle" font-family="Lato, sans-serif" font-size="24" fill="#6f6f71">@</text>
        </svg>
        website/blog
      </li>
      <li class="contact-item">
        <svg class="contact-icon" viewBox="0 0 28 28" aria-hidden="true">
          <rect x="2" y="7" width="24" height="15" fill="#6f6f71"/>
          <polyline points="2,7 14,16 26,7" fill="none" stroke="#f6f7f9" stroke-width="1.5"/>
        </svg>
        Email
      </li>
      <li class="contact-item">
        <svg class="contact-icon" viewBox="0 0 28 28" aria-hidden="true">
          <circle cx="14" cy="14" r="11" fill="#6f6f71"/>
        </svg>
        Social username
      </li>
    </ul>
  </section>

</div>
</body>
</html>
```